I need a wordpress website for myconsulting company specialized in data privacy

I'm looking for a wordpress website for my consulting company specialized in data privacy (GDPR) and computer science.
The website will serve as entry point to for potential clients.
The website should have the following sections (I'm opened to new ideas):
- Presentation of the company
- General presentation
- Services provided with some details
- Blog/articles with tags (if possible)
- Contact
On every page of the website there should be some references to pages (such as privacy policy, legal information...)
If possible he website should be multinlingual (english and french). I'll personnally take care of the translation in french.
Regarding branding;
- Name of the company: Laurent Dubreuil Conseil
- Logo is attached
- For colors to be used see attached PDF for exemple

```html
<!DOCTYPE html>
<html lang="en">
<head>
<meta charset="utf-8">
<title>Laurent Dubreuil Conseil – Data Privacy Consulting</title>
<link rel="stylesheet" href="https://fonts.googleapis.com/css2?family=Montserrat:wght@500;600;700;800&family=Roboto:wght@400;500&display=swap">
<style>
:root{
  --navy:#0c2a45;
  --ink:#1b3150;
  --teal:#137886;
  --teal-dark:#0f6573;
  --text:#3b3f46;
  --muted:#f1f2f4;
  --white:#ffffff;
  --line:#c9ced6;
}
*{box-sizing:border-box;margin:0;padding:0}
html,body{width:1200px;height:3250px;overflow:hidden}
body{position:relative;background:var(--white);font-family:"Roboto",Arial,sans-serif;color:var(--text)}
.abs{position:absolute}
.btn{position:absolute;display:flex;align-items:center;justify-content:center;border-radius:20px;background:var(--teal);color:var(--white);font-family:"Montserrat",Arial,sans-serif;font-weight:700;font-size:11px;letter-spacing:.2px;text-decoration:none;white-space:nowrap}
.btn.navy{background:var(--navy)}
.btn.light{background:var(--white);color:var(--teal)}

/* header */
.brand{position:absolute;left:130px;top:40px;display:flex;align-items:center;gap:12px}
.brand-mark{width:26px;height:26px;background:var(--teal)}
.brand-name{font-family:"Montserrat",Arial,sans-serif;font-weight:600;font-size:19px;color:var(--teal)}
.nav{position:absolute;top:24px;left:496px;font-family:"Montserrat",Arial,sans-serif;font-weight:600;font-size:14px;color:var(--navy)}
.nav a{position:absolute;white-space:nowrap;color:var(--navy);text-decoration:none}
.nav a.active{color:var(--teal);border-bottom:2px solid var(--teal);padding-bottom:4px}
.lang{position:absolute;left:1000px;top:18px;width:72px;height:28px;border:1.5px solid var(--navy);border-radius:8px;font:500 11px "Montserrat",Arial,sans-serif;color:var(--navy);display:flex;align-items:center;justify-content:center}

/* hero */
.hero-photo{position:absolute;left:0;top:72px;width:1200px;height:531px;background:linear-gradient(120deg,#5c6462 0%,#b9bdbb 35%,#d8d6d0 55%,#8a8f93 80%,#4c5558 100%)}
.hero-title{position:absolute;left:870px;top:372px;font:800 40px/44px "Montserrat",Arial,sans-serif;color:var(--white);letter-spacing:.5px}
.hero-arrows{position:absolute;left:698px;top:558px}

/* welcome */
.welcome-photo{position:absolute;left:131px;top:654px;width:405px;height:357px;border-radius:40px;background:radial-gradient(circle at 55% 55%,#3aa6d8 0%,#1b4f86 28%,#1c1f3d 60%,#2a0f1c 100%)}
.eyebrow{position:absolute;left:575px;top:650px;font:600 18px "Montserrat",Arial,sans-serif;color:var(--navy)}
.eyebrow::after{content:"";position:absolute;left:0;top:26px;width:112px;height:2px;background:var(--teal)}
.welcome-title{position:absolute;left:573px;top:684px;font:600 30px "Montserrat",Arial,sans-serif;color:var(--navy);white-space:nowrap}
.welcome-title::after{content:"";position:absolute;left:2px;top:44px;width:108px;height:2px;background:var(--teal)}
.welcome-copy{position:absolute;left:576px;top:757px;width:489px;font-size:13.5px;line-height:20.8px;text-align:justify;color:#333}

/* services */
.services{position:absolute;left:0;top:1060px;width:1200px;height:565px;background:var(--muted)}
.section-title{position:absolute;width:1200px;left:0;text-align:center;font:700 24px "Montserrat",Arial,sans-serif;color:var(--navy)}
.rule{position:absolute;height:3px;background:var(--teal)}
.service{position:absolute;top:1188px;width:222px;height:367px;border-radius:111px;background:var(--white);box-shadow:0 8px 22px rgba(20,40,70,.10);text-align:center}
.service.featured{background:linear-gradient(180deg,#1a8a9c 0%,#147686 60%,#0f6170 100%)}
.service .icon{position:absolute;left:66px;top:34px;width:90px;height:90px;border-radius:50%;background:var(--navy);display:flex;align-items:center;justify-content:center}
.service.teal .icon{background:var(--teal)}
.service.featured .icon{background:var(--white)}
.service h3{position:absolute;top:148px;width:100%;font:700 16px "Montserrat",Arial,sans-serif;color:var(--navy)}
.service.teal h3{color:var(--teal)}
.service.featured h3{color:var(--white)}
.service p{position:absolute;top:182px;left:16px;width:190px;font-size:12.5px;line-height:17.5px;color:#333;white-space:nowrap}
.service.featured p{color:#e3f2f4}
.service .btn{left:66px;top:296px;width:90px;height:28px;font-size:10.5px}

/* blog */
.blog-band{position:absolute;left:0;top:1595px;width:1200px;height:290px}
.blog-title{position:absolute;left:130px;top:1688px;font:700 24px "Montserrat",Arial,sans-serif;color:var(--white)}
.blog-rule{position:absolute;left:131px;width:44px;height:3px;background:var(--white)}
.post{position:absolute;top:1792px;width:298px;height:385px;background:var(--white);border-radius:6px;box-shadow:0 6px 20px rgba(20,40,70,.12)}
.post .thumb{position:absolute;left:18px;top:18px;width:262px;height:154px}
.post .date{position:absolute;left:27px;top:192px;font-size:11.5px;text-decoration:underline;color:#333}
.post h4{position:absolute;left:27px;top:212px;width:245px;font:700 14.5px/17.5px "Montserrat",Arial,sans-serif;color:var(--navy)}
.post p{position:absolute;left:27px;top:262px;width:250px;font-size:12.2px;line-height:17.5px;color:#444}
.post .btn{left:26px;top:330px;width:91px;height:28px;font-size:10.5px}

/* contact */
.contact-photo{position:absolute;left:130px;top:2325px}
.info{position:absolute;left:684px;display:flex;gap:18px}
.info .dot{width:38px;height:38px;border-radius:50%;background:var(--teal);display:flex;align-items:center;justify-content:center;flex:none;margin-top:2px}
.info b{display:block;font:500 14px "Roboto",Arial,sans-serif;color:var(--navy)}
.info span{font-size:16px;color:#222}
.field{position:absolute;left:689px;width:383px;height:46px;border:2px solid var(--line);border-radius:8px;padding:14px 18px;font-size:13px;color:#333}
.send{position:absolute;left:689px;top:2789px;width:383px;height:46px;border-radius:8px;background:var(--teal);color:var(--white);font:700 15px "Montserrat",Arial,sans-serif;display:flex;align-items:center;justify-content:center}
.follow{position:absolute;left:690px;top:2885px;font:500 13px "Roboto",Arial,sans-serif;color:#222}
.social{position:absolute;top:2922px;width:46px;height:46px;border-radius:50%;box-shadow:0 6px 10px rgba(0,0,0,.18)}

/* footer */
.footer-wave{position:absolute;left:0;top:2820px}
.footer-brand{position:absolute;left:150px;top:3050px;width:290px;text-align:center;font:600 22px "Montserrat",Arial,sans-serif;color:var(--white);white-space:nowrap}
.footer-links{position:absolute;font:500 11.5px "Montserrat",Arial,sans-serif;color:var(--white);white-space:nowrap}
.copyright{position:absolute;left:190px;top:3208px;font-size:11.5px;color:var(--white)}
</style>
</head>
<body>

<header>
  <div class="brand"><span class="brand-mark"></span><span class="brand-name">Laurent Dubreuil Conseil</span></div>
  <nav class="nav">
    <a class="active" style="left:0">HOME</a>
    <a style="left:87px">ABOUT US</a>
    <a style="left:209px">SERVICES</a>
    <a style="left:326px">BLOG</a>
    <a style="left:408px">CONTACT</a>
  </nav>
  <div class="lang">EN&nbsp;▾</div>
</header>

<section>
  <div class="hero-photo" role="img" aria-label="Overhead view of a consulting team meeting around a white table with laptops and notebooks"></div>
  <svg class="abs" style="left:0;top:72px" width="1200" height="531" viewBox="0 0 1200 531">
    <polygon points="0,0 588,0 568,50 0,50" fill="#fff"/>
    <polygon points="765,531 790,481 1200,481 1200,531" fill="#fff"/>
  </svg>
  <h1 class="hero-title">DATA PRIVACY<br>CONSULTING</h1>
  <a class="btn" style="left:870px;top:476px;width:132px;height:40px;font-size:14px">READ MORE</a>
  <svg class="hero-arrows" width="60" height="26" viewBox="0 0 60 26">
    <path d="M9 5 L3 13 L9 21" stroke="#fff" stroke-width="2.5" fill="none"/>
    <path d="M44 5 L50 13 L44 21" stroke="#fff" stroke-width="2.5" fill="none"/>
  </svg>
</section>

<section>
  <div class="welcome-photo" role="img" aria-label="Hands sheltering a glowing digital security shield"></div>
  <div class="eyebrow">Welcome to</div>
  <h2 class="welcome-title">Laurent Dubreuil Conseil</h2>
  <p class="welcome-copy">Sed ut perspiciatis unde omnis iste natus error sit voluptatem accusantium doloremque laudantium, totam rem aperiam, eaque ipsa quae ab illo inventore veritatis et quasi architecto beatae vitae dicta sunt explicabo. Nemo enim ipsam voluptatem quia voluptas sit aspernatur aut odit aut fugit, sed quia consequuntur magni dolores eos qui ratione voluptatem sequi nesciunt. Neque porro quisquam est, qui dolorem ipsum quia dolor sit amet, consectetur, adipisci velit, sed quia non numquam eius modi tempora incidunt ut labore et dolore magnam aliquam quaerat voluptatem. Ut enim ad minima veniam, quis nostrum exercitationem.</p>
  <a class="btn" style="left:578px;top:977px;width:100px;height:32px">READ MORE</a>
</section>

<section>
  <div class="services"></div>
  <h2 class="section-title" style="top:1119px">OUR SERVICES</h2>
  <div class="rule" style="left:578px;top:1165px;width:44px"></div>

  <article class="service" style="left:131px">
    <div class="icon"><svg width="40" height="44" viewBox="0 0 40 44"><path d="M20 2 L37 8 V20 C37 31 29 39 20 42 C11 39 3 31 3 20 V8 Z" fill="#fff"/><rect x="13" y="20" width="14" height="11" rx="1.5" fill="#0c2a45"/><path d="M15.5 20 V16 a4.5 4.5 0 0 1 9 0 V20" stroke="#0c2a45" stroke-width="2.5" fill="none"/></svg></div>
    <h3>Data Privacy</h3>
    <p>Sed ut perspiciatis unde<br>omnis iste natus error sit<br>voluptatem accusantium<br>doloremque laudan<br>tium totam.</p>
    <a class="btn navy">READ MORE</a>
  </article>

  <article class="service featured" style="left:372px">
    <div class="icon"><svg width="48" height="44" viewBox="0 0 48 44"><circle cx="15" cy="20" r="7" fill="#137886"/><path d="M2 42 C2 32 8 29 15 29 C22 29 28 32 28 42 Z" fill="#137886"/><rect x="22" y="2" width="24" height="16" rx="3" fill="#137886"/><path d="M27 18 L25 24 L32 18 Z" fill="#137886"/><circle cx="29" cy="10" r="1.6" fill="#fff"/><circle cx="34" cy="10" r="1.6" fill="#fff"/><circle cx="39" cy="10" r="1.6" fill="#fff"/></svg></div>
    <h3>Consulting</h3>
    <p>Sed ut perspiciatis unde<br>omnis iste natus error sit<br>voluptatem accusantium<br>doloremque laudan<br>tium totam.</p>
    <a class="btn light">READ MORE</a>
  </article>

  <article class="service" style="left:611px">
    <div class="icon"><svg width="44" height="44" viewBox="0 0 44 44"><path d="M6 24 V20 a16 16 0 0 1 32 0 V24" stroke="#fff" stroke-width="3.5" fill="none"/><rect x="3" y="21" width="9" height="14" rx="3" fill="#fff"/><rect x="32" y="21" width="9" height="14" rx="3" fill="#fff"/><path d="M36 35 C36 40 30 41 24 41" stroke="#fff" stroke-width="2.5" fill="none"/><rect x="18" y="38" width="8" height="5" rx="2" fill="#fff"/></svg></div>
    <h3>Support</h3>
    <p>Sed ut perspiciatis unde<br>omnis iste natus error sit<br>voluptatem accusantium<br>doloremque laudan<br>tium totam.</p>
    <a class="btn navy">READ MORE</a>
  </article>

  <article class="service teal" style="left:849px">
    <div class="icon"><svg width="46" height="44" viewBox="0 0 46 44"><circle cx="23" cy="7" r="5" fill="#fff"/><circle cx="10" cy="11" r="4" fill="#fff"/><circle cx="36" cy="11" r="4" fill="#fff"/><rect x="17" y="14" width="12" height="18" rx="3" fill="#fff"/><rect x="19" y="30" width="8" height="13" fill="#fff"/><rect x="5" y="17" width="9" height="14" rx="3" fill="#fff"/><rect x="32" y="17" width="9" height="14" rx="3" fill="#fff"/><rect x="7" y="29" width="5" height="11" fill="#fff"/><rect x="34" y="29" width="5" height="11" fill="#fff"/></svg></div>
    <h3>Expert Team</h3>
    <p>Sed ut perspiciatis unde<br>omnis iste natus error sit<br>voluptatem accusantium<br>doloremque laudan<br>tium totam.</p>
    <a class="btn">READ MORE</a>
  </article>
</section>

<section>
  <svg class="blog-band" viewBox="0 0 1200 290" width="1200" height="290">
    <defs>
      <linearGradient id="bandGrad" x1="0" y1="0" x2="1" y2="0">
        <stop offset="0" stop-color="#13174a"/>
        <stop offset=".55" stop-color="#2a2a6e"/>
        <stop offset="1" stop-color="#2d4a8a"/>
      </linearGradient>
    </defs>
    <polygon points="0,30 940,30 952,0 1200,0 1200,290 0,290" fill="url(#bandGrad)"/>
  </svg>
  <div class="abs" role="img" aria-label="Hand touching a digital padlock with data protection graphics" style="left:700px;top:1595px;width:500px;height:290px;background:linear-gradient(100deg,rgba(45,42,110,0) 0%,rgba(60,80,150,.55) 45%,rgba(80,120,180,.6) 100%);clip-path:polygon(240px 30px,240px 0,500px 0,500px 290px,0 290px,0 30px)"></div>
  <div class="blog-rule" style="top:1674px"></div>
  <h2 class="blog-title">LATEST BLOG</h2>
  <div class="blog-rule" style="top:1735px"></div>

  <article class="post" style="left:131px">
    <div class="thumb" role="img" aria-label="Business team seated around a meeting table" style="background:linear-gradient(135deg,#8c9298,#5a6168 60%,#3a4046)"></div>
    <span class="date">21 Feb 2022</span>
    <h4>Lorem ipsum dolor sit amet consectetur</h4>
    <p>Sed ut perspiciatis unde omnis iste natus error sit voluptatem accusantium dolo remque laudan lorem ipsum.</p>
    <a class="btn">READ MORE</a>
  </article>

  <article class="post" style="left:452px">
    <div class="thumb" role="img" aria-label="Two colleagues reviewing a tablet by a window" style="background:linear-gradient(135deg,#d8dde0,#7d858c 55%,#2d3238)"></div>
    <span class="date">21 Feb 2022</span>
    <h4>Sed ut perspiciatis unde omnis iste natus error sit</h4>
    <p>Sed ut perspiciatis unde omnis iste natus error sit voluptatem accusantium dolo remque laudan lorem ipsum.</p>
    <a class="btn">READ MORE</a>
  </article>

  <article class="post" style="left:772px">
    <div class="thumb" role="img" aria-label="Team brainstorming with colourful sticky notes" style="background:linear-gradient(135deg,#c9a7a0,#6b7f9a 50%,#394456)"></div>
    <span class="date">21 Feb 2022</span>
    <h4>But I must explain to you how all this mistaken idea of deno</h4>
    <p>Sed ut perspiciatis unde omnis iste natus error sit voluptatem accusantium dolo remque laudan lorem ipsum.</p>
    <a class="btn">READ MORE</a>
  </article>
</section>

<section>
  <h2 class="section-title" style="top:2232px">CONTACT US</h2>
  <div class="rule" style="left:578px;top:2279px;width:44px"></div>

  <svg class="contact-photo" width="500" height="490" viewBox="0 0 500 490" role="img" aria-label="Consulting team meeting in a bright office around a conference table">
    <defs>
      <linearGradient id="officeGrad" x1="0" y1="0" x2="0" y2="1">
        <stop offset="0" stop-color="#eef0f0"/>
        <stop offset=".5" stop-color="#b9bfc4"/>
        <stop offset="1" stop-color="#6a737c"/>
      </linearGradient>
    </defs>
    <path d="M120 40 C180 20 240 10 300 30 C360 50 380 80 410 120 C440 160 510 200 490 260 C470 320 430 370 380 420 C330 470 250 490 190 450 C140 415 60 400 25 330 C0 280 20 220 50 170 C80 120 70 60 120 40 Z" fill="url(#officeGrad)"/>
    <path d="M3 240 C40 170 110 90 190 40 C240 10 290 20 330 60 C390 120 450 190 480 240 C500 280 470 320 420 370 C360 430 300 480 240 478 C200 476 160 450 120 420 C70 380 -10 290 3 240 Z" fill="none" stroke="#137886" stroke-width="5"/>
  </svg>

  <div class="info" style="top:2306px"><span class="dot"><svg width="14" height="18" viewBox="0 0 14 18"><path d="M7 0 C3 0 0 3 0 7 C0 12 7 18 7 18 C7 18 14 12 14 7 C14 3 11 0 7 0 Z" fill="#fff"/><circle cx="7" cy="7" r="2.5" fill="#137886"/></svg></span><div><b>Address</b><span>27 Maple Row, Dalton, GA 30720</span></div></div>
  <div class="info" style="top:2373px"><span class="dot"><svg width="16" height="16" viewBox="0 0 16 16"><path d="M3 1 L6 1 L7 5 L5 6.5 C6 9 7 10 9.5 11 L11 9 L15 10 L15 13 C15 14 14 15 13 15 C6 15 1 10 1 3 C1 2 2 1 3 1 Z" fill="#fff"/></svg></span><div><b>Call Us</b><span>+1 555 014 2290</span></div></div>
  <div class="info" style="top:2437px"><span class="dot"><svg width="16" height="12" viewBox="0 0 16 12"><rect x="0" y="0" width="16" height="12" rx="1.5" fill="#fff"/><path d="M1 1 L8 7 L15 1" stroke="#137886" stroke-width="1.6" fill="none"/></svg></span><div><b>Email Us</b><span>hello@dubreuilconseil.example</span></div></div>

  <div class="field" style="top:2508px">Full Name</div>
  <div class="field" style="top:2565px">Email id</div>
  <div class="field" style="top:2622px">Phone</div>
  <div class="field" style="top:2679px;height:92px">Message</div>
  <div class="send">SEND MESSAGE</div>
</section>

<footer>
  <svg class="footer-wave" width="1200" height="430" viewBox="0 0 1200 430">
    <path d="M0 45 C250 -20 420 30 560 120 C720 220 850 300 1200 260 L1200 430 L0 430 Z" fill="#137886"/>
    <path d="M0 75 C250 20 410 60 540 150 C700 260 850 340 1200 320 L1200 430 L0 430 Z" fill="#0c2a45"/>
    <path d="M1200 330 C980 350 900 300 800 250 C900 330 1020 380 1200 395 Z" fill="#1a8a9c" opacity=".85"/>
  </svg>
  <div class="follow">FOLLOW US</div>
  <span class="social" aria-label="Social profile link 1" style="left:692px;background:#2f4fa3"></span>
  <span class="social" aria-label="Social profile link 2" style="left:750px;background:#e4405f"></span>
  <span class="social" aria-label="Social profile link 3" style="left:807px;background:#1d9bf0"></span>

  <div class="footer-brand">Laurent Dubreuil Conseil</div>
  <div class="footer-links" style="left:217px;top:3133px">PRIVACY POLICY &nbsp;|&nbsp; LEGAL</div>
  <div class="footer-links" style="left:128px;top:3162px">HOME &nbsp;&nbsp;&nbsp;&nbsp; ABOUT US &nbsp;&nbsp;&nbsp;&nbsp; SERVICES &nbsp;&nbsp;&nbsp;&nbsp; BLOG &nbsp;&nbsp;&nbsp;&nbsp; CONTACT</div>
  <div class="copyright">Copyright © 2022 All Rights Reserved</div>
</footer>

</body>
</html>
```